Podcast Marketing Template for LinkedIn

I would like to have graphics to post notices of new podcast episodes on LinkedIn as release new episodes.
The graphics need to be in a template form that can be easily updated by my VA.
Each episode will have a new title and guest.
Two examples of a ROUGH DRAFT of an episode example are attached.
(I do not like these because I think they reflect the standards I have for my brand.)
The posts should be bright and clean and clearly reflect QUALITY of the podcast in the quality of the design. Audience and interviewees are CEOs.
Please refer to my website and podcast art to see brand direction.
www.lorenbriskadvisory.com
Each

```html
<!DOCTYPE html>
<html lang="en">
<head>
<meta charset="utf-8">
<title>Podcast Episode Template</title>
<link rel="stylesheet" href="https://fonts.googleapis.com/css2?family=Lexend:wght@500;600&family=Arimo:wght@400;700&display=swap">
<style>
  :root {
    --ink: #000000;
    --paper: #ffffff;
    --brand-blue: #1aa3dc;
    --deep-blue: #0f3f66;
    --steel: #3b4652;
    --muted: #cfd6dc;
  }
  * { box-sizing: border-box; margin: 0; padding: 0; }
  html, body { width: 1200px; height: 1155px; overflow: hidden; background: var(--paper); }
  body { position: relative; font-family: "Arimo", Arial, sans-serif; }

  .sheet-header {
    position: absolute; left: 0; top: 0; width: 1200px; height: 269px;
    background: var(--ink); color: var(--paper);
  }
  .sheet-title {
    position: absolute; left: 56px; top: 30px;
    font-family: "Lexend", sans-serif; font-weight: 600; font-size: 66px; letter-spacing: 1px;
  }
  .sheet-subtitle {
    position: absolute; left: 56px; top: 136px;
    font-family: "Lexend", sans-serif; font-weight: 500; font-size: 46px; color: var(--brand-blue);
  }
  .sheet-size {
    position: absolute; left: 56px; top: 186px;
    font-family: "Lexend", sans-serif; font-weight: 500; font-size: 32px;
  }
  .header-brand {
    position: absolute; right: 70px; top: 70px; width: 270px;
    display: flex; align-items: center; gap: 18px;
  }
  .header-brand .brand-dot {
    width: 110px; height: 110px; border-radius: 50%; background: var(--brand-blue); flex: none;
  }
  .header-brand .brand-name {
    font-family: "Lexend", sans-serif; font-weight: 600; font-size: 26px; line-height: 1.15; color: var(--paper);
  }

  .episode-card {
    position: absolute; width: 530px; height: 298px; overflow: hidden; background: var(--ink);
  }
  .card-a { left: 46px; top: 386px; }
  .card-b { left: 629px; top: 386px; }
  .card-c { left: 46px; top: 744px; }
  .card-d { left: 629px; top: 744px; }

  .card-band {
    position: absolute; left: 0; top: 0; width: 100%; height: 81px;
    background: var(--ink); border-bottom: 2px solid var(--brand-blue); z-index: 2;
  }
  .band-label {
    position: absolute; left: 20px; top: 10px;
    font-family: "Lexend", sans-serif; font-weight: 600; font-size: 22px; color: var(--paper);
  }
  .show-name {
    position: absolute; left: 20px; top: 42px;
    font-family: "Arimo", sans-serif; font-weight: 700; font-size: 15px; color: var(--brand-blue);
  }
  .show-tagline {
    position: absolute; left: 20px; top: 60px;
    font-size: 11px; color: var(--paper); letter-spacing: 0.3px;
  }
  .band-mark {
    position: absolute; right: 28px; top: 10px; width: 58px; height: 58px;
    border-radius: 50%; border: 6px solid var(--brand-blue);
  }

  .card-backdrop { position: absolute; left: 0; top: 83px; width: 100%; height: 215px; }
  .card-a .card-backdrop { background: linear-gradient(90deg, #050505 30%, #1b2a38 62%, #5a6066 100%); }
  .card-b .card-backdrop { background: linear-gradient(90deg, #0a0a0a 20%, var(--deep-blue) 55%, #7b7f82 78%, #2a2c2e 100%); }
  .card-c .card-backdrop { background: linear-gradient(90deg, #050505 30%, var(--deep-blue) 60%, #2f3a44 85%, #444 100%); }
  .card-d .card-backdrop { background: linear-gradient(180deg, #1a5c8f 0%, #123c5e 60%, #0b2238 100%); }

  .backdrop-icon { position: absolute; z-index: 1; opacity: 0.55; }

  .episode-title {
    position: absolute; left: 24px; top: 92px; z-index: 2;
    font-family: "Lexend", sans-serif; font-weight: 500; font-size: 37px; line-height: 36px; color: var(--paper);
  }

  .guest { position: absolute; left: 26px; top: 216px; z-index: 2; display: flex; align-items: center; gap: 14px; }
  .guest-photo {
    width: 62px; height: 62px; border-radius: 50%;
    border: 3px solid var(--brand-blue);
    background: radial-gradient(circle at 50% 40%, #b89a86 0%, #6d5a4e 60%, #2d3a44 100%);
  }
  .guest-name { font-size: 9px; color: var(--paper); }
  .guest-role { font-size: 9px; color: var(--brand-blue); margin-top: 2px; }

  .card-brand {
    position: absolute; right: 16px; bottom: 14px; z-index: 2;
    display: flex; align-items: center; gap: 7px;
  }
  .card-brand .brand-dot { width: 26px; height: 26px; border-radius: 50%; background: var(--brand-blue); }
  .card-brand .brand-name {
    font-family: "Lexend", sans-serif; font-weight: 600; font-size: 12px; line-height: 13px; color: var(--paper);
  }
</style>
</head>
<body>

<header class="sheet-header">
  <h1 class="sheet-title">PODCAST</h1>
  <p class="sheet-subtitle">TEMPLATE</p>
  <p class="sheet-size">1920X1080PX</p>
  <div class="header-brand">
    <span class="brand-dot"></span>
    <span class="brand-name">LOREN BRISK<br>ADVISORY</span>
  </div>
</header>

<section class="episode-card card-a">
  <div class="card-band">
    <p class="band-label">PODCAST</p>
    <p class="show-name">BUILDING MOMENTUM</p>
    <p class="show-tagline">A CEO GROWTH AND LEGACY</p>
    <span class="band-mark"></span>
  </div>
  <div class="card-backdrop" role="img" aria-label="Blue-tinted photo of a handshake between business people"></div>
  <svg class="backdrop-icon" style="left:360px;top:110px" width="130" height="140" viewBox="0 0 130 140">
    <g fill="#9aa2a8">
      <polygon points="30,40 50,15 70,40 58,40 58,70 42,70 42,40"/>
      <polygon points="70,30 92,5 114,30 101,30 101,70 83,70 83,30"/>
      <rect x="10" y="90" width="110" height="22" rx="8"/>
    </g>
  </svg>
  <h2 class="episode-title">Technology a<br>Philanthropy<br>in Education</h2>
  <div class="guest">
    <div class="guest-photo" role="img" aria-label="Guest portrait"></div>
    <div><p class="guest-name">With Daniel Morrow</p><p class="guest-role">CEO of Kestrel</p></div>
  </div>
  <div class="card-brand"><span class="brand-dot"></span><span class="brand-name">LOREN BRISK<br>ADVISORY</span></div>
</section>

<section class="episode-card card-b">
  <div class="card-band">
    <p class="band-label">PODCAST</p>
    <p class="show-name">BUILDING MOMENTUM</p>
    <p class="show-tagline">A CEO GROWTH AND LEGACY</p>
    <span class="band-mark"></span>
  </div>
  <div class="card-backdrop" role="img" aria-label="Blue-tinted photo of hands using a tablet with charts"></div>
  <svg class="backdrop-icon" style="left:380px;top:100px" width="140" height="140" viewBox="0 0 140 140">
    <g fill="none" stroke="#b0b6ba" stroke-width="12">
      <circle cx="70" cy="70" r="58"/><circle cx="70" cy="70" r="34"/>
    </g>
    <circle cx="70" cy="70" r="12" fill="#b0b6ba"/>
  </svg>
  <h2 class="episode-title">Technology a<br>Philanthropy<br>in Education</h2>
  <div class="guest">
    <div class="guest-photo" role="img" aria-label="Guest portrait"></div>
    <div><p class="guest-name">With Daniel Morrow</p><p class="guest-role">CEO of Kestrel</p></div>
  </div>
  <div class="card-brand"><span class="brand-dot"></span><span class="brand-name">LOREN BRISK<br>ADVISORY</span></div>
</section>

<section class="episode-card card-c">
  <div class="card-band">
    <p class="band-label">PODCAST</p>
    <p class="show-name">BUILDING MOMENTUM</p>
    <p class="show-tagline">A CEO GROWTH AND LEGACY</p>
    <span class="band-mark"></span>
  </div>
  <div class="card-backdrop" role="img" aria-label="Blue-tinted photo of a laptop showing market data"></div>
  <svg class="backdrop-icon" style="left:370px;top:100px" width="140" height="160" viewBox="0 0 140 160">
    <g stroke="#9aa2a8" stroke-width="16" fill="#9aa2a8">
      <line x1="10" y1="100" x2="85" y2="30"/>
      <line x1="55" y1="150" x2="120" y2="90"/>
    </g>
    <g fill="#9aa2a8">
      <polygon points="70,15 115,5 105,50"/>
      <polygon points="105,75 138,65 130,110"/>
    </g>
  </svg>
  <h2 class="episode-title">Technology a<br>Philanthropy<br>in Education</h2>
  <div class="guest">
    <div class="guest-photo" role="img" aria-label="Guest portrait"></div>
    <div><p class="guest-name">With Daniel Morrow</p><p class="guest-role">CEO of Kestrel</p></div>
  </div>
  <div class="card-brand"><span class="brand-dot"></span><span class="brand-name">LOREN BRISK<br>ADVISORY</span></div>
</section>

<section class="episode-card card-d">
  <div class="card-band">
    <p class="band-label">PODCAST</p>
    <p class="show-name">BUILDING MOMENTUM</p>
    <p class="show-tagline">A CEO GROWTH AND LEGACY</p>
    <span class="band-mark"></span>
  </div>
  <div class="card-backdrop" role="img" aria-label="Blue-tinted photo of a city skyline at night"></div>
  <svg class="backdrop-icon" style="left:370px;top:100px" width="140" height="110" viewBox="0 0 140 110">
    <rect x="5" y="5" width="130" height="88" rx="10" fill="none" stroke="#b0b6ba" stroke-width="8"/>
    <g fill="#b0b6ba">
      <rect x="28" y="48" width="12" height="34"/>
      <rect x="50" y="34" width="12" height="48"/>
      <rect x="72" y="56" width="12" height="26"/>
      <rect x="94" y="24" width="12" height="58"/>
    </g>
  </svg>
  <h2 class="episode-title">Technology a<br>Philanthropy<br>in Education</h2>
  <div class="guest">
    <div class="guest-photo" role="img" aria-label="Guest portrait"></div>
    <div><p class="guest-name">With Daniel Morrow</p><p class="guest-role">CEO of Kestrel</p></div>
  </div>
  <div class="card-brand"><span class="brand-dot"></span><span class="brand-name">LOREN BRISK<br>ADVISORY</span></div>
</section>

</body>
</html>
```